Brightmoor Academy - Personal Development business 2.0 needs a social post format design.

https://www.brightmooracademy.example

Our focus with Brightmoor Academy is on developing people through knowledge and skills to improve their everyday lives.
We love simplicity, Quorel design and less is more.

We are crazy about personal growth, science, design, the latest gadgets and people.

We need 4 formats for our social media posts.
1. Blogs -to pronounce a blog post
2. Workshop /training - to pronounce our workshops/trainings (both online and offline)
3. Podcast - called "Wissel je blik". To pronounce a guest we've spoken. The host is called Berend.
4. Facts - to pronounce short facts about personal development. Invites people to read more.
The formats should include: high quality pictogram (better than the uploaded picto's), 1 of the 3 logo's in the design.
It's important that we can edit the design in Lumora Draw / Lumora Pixel to adjust the text in the format.

Attached you find four of our current designs, which are a poor example of how the designs should look like. These are just to show you how much lines of text (more or less) will be in the designs. So please do not make a design that looks like these ;) You have carte blanche.

Our customers are mostly women (80%). We focus on both business and casual customers.

Target Market(s)

80% woman, 20% men. We focus on both business and casual customers.

Requirements
Must have
• Less is more. Quorel Design alike. Simplicity.
Aimed at the women target audience.
Designs must be edible for adjusting the text in the format.
Nice to have
• Unique concept.
The design should "breathe".
Each design can have a different color, so customers identify the specific post with specific information. For example, blog is red, workshop post black, etc.

```html
<!DOCTYPE html>
<html lang="nl">
<head>
<meta charset="utf-8">
<title>Brightmoor Academy – social post formats</title>
<link href="https://fonts.googleapis.com/css2?family=Fira+Sans+Condensed:wght@400;600;700&display=swap" rel="stylesheet">
<style>
  :root {
    --page: #ebebeb;
    --white: #ffffff;
    --training-bg: #2d2d2d;
    --training-photo: #5a5a5a;
    --training-band: #1e1e1e;
    --training-sliver: #3f4444;
    --blog-bg: #f6c21f;
    --blog-photo: #f08a12;
    --blog-band: #fb7b08;
    --blog-sliver: #fb9a45;
    --facts-bg: #00c874;
    --facts-photo: #04281a;
    --facts-band: #0a7a45;
    --facts-sliver: #6fcd9c;
    --podcast-bg: #0d4f8c;
    --podcast-photo: #2a8ad8;
    --podcast-band: #0b7bc8;
    --podcast-sliver: #6d9ed8;
  }
  * { box-sizing: border-box; margin: 0; padding: 0; }
  html, body { width: 1200px; height: 600px; overflow: hidden; background: var(--page); }
  body { position: relative; font-family: "Fira Sans Condensed", sans-serif; color: var(--white); }

  .post { position: absolute; top: 165px; width: 271px; height: 271px; overflow: hidden; }
  .post--training { left: 20px; }
  .post--blog { left: 316px; }
  .post--facts { left: 613px; }
  .post--podcast { left: 909px; }

  .post__photo { position: absolute; inset: 0; }
  .post--training .post__photo { background: radial-gradient(circle at 72% 38%, var(--training-photo) 0%, var(--training-bg) 62%); }
  .post--blog .post__photo { background: linear-gradient(135deg, var(--blog-bg) 20%, #f7b21a 55%, var(--blog-photo) 100%); }
  .post--facts .post__photo { background: linear-gradient(100deg, var(--facts-bg) 35%, #049a58 60%, var(--facts-photo) 100%); }
  .post--podcast .post__photo { background: radial-gradient(circle at 72% 40%, var(--podcast-photo) 0%, var(--podcast-bg) 65%); }

  .post__curve { position: absolute; inset: 0; width: 271px; height: 271px; }
  .post--training .band { fill: var(--training-band); } .post--training .sliver { fill: var(--training-sliver); }
  .post--blog .band { fill: var(--blog-band); } .post--blog .sliver { fill: var(--blog-sliver); }
  .post--facts .band { fill: var(--facts-band); } .post--facts .sliver { fill: var(--facts-sliver); }
  .post--podcast .band { fill: var(--podcast-band); } .post--podcast .sliver { fill: var(--podcast-sliver); }

  .brand { position: absolute; left: 21px; top: 24px; font-size: 13px; font-weight: 400; letter-spacing: 0.2px; }

  .headline { position: absolute; left: 21px; font-weight: 700; font-size: 23.5px; line-height: 21px; }
  .post--training .headline { top: 70px; text-transform: uppercase; }
  .post--blog .headline, .post--facts .headline { top: 84px; }
  .post--podcast .headline { top: 106px; text-transform: uppercase; }

  .subline { position: absolute; left: 21px; font-weight: 400; font-size: 15px; line-height: 15px; }
  .post--training .subline { top: 139px; }
  .post--podcast .subline { top: 70px; }

  .format { position: absolute; right: 18px; bottom: 16px; display: flex; align-items: center; gap: 7px; }
  .format__label { font-family: "Fira Sans Condensed", sans-serif; font-size: 8px; line-height: 9px; font-weight: 400; text-align: right; color: var(--white); }
  .format__icon { width: 28px; height: 28px; }
  .format__icon * { stroke: var(--white); fill: none; stroke-width: 2; stroke-linecap: round; stroke-linejoin: round; }
  .format__icon .solid { fill: var(--white); stroke: none; }
</style>
</head>
<body>

<article class="post post--training">
  <div class="post__photo" role="img" aria-label="Black and white portrait of the trainer"></div>
  <svg class="post__curve" viewBox="0 0 271 271" aria-hidden="true">
    <path class="band" d="M0 271 L0 238 C60 230 150 216 195 192 C230 174 255 156 271 140 L271 271 Z"/>
    <path class="sliver" d="M0 238 C60 230 140 219 190 208 C120 236 50 256 0 271 Z"/>
  </svg>
  <div class="brand">Brightmoor Academy</div>
  <h2 class="headline">Pre-new<br>year’s<br>eve</h2>
  <p class="subline">Dinsdag<br>29dec<br>19-21u</p>
  <div class="format">
    <span class="format__label">online<br>training</span>
    <svg class="format__icon" viewBox="0 0 28 28" aria-hidden="true">
      <rect x="3" y="5" width="22" height="14" rx="1.5"/>
      <path d="M10 24 H18"/>
      <path d="M14 19 V24"/>
    </svg>
  </div>
</article>

<article class="post post--blog">
  <div class="post__photo" role="img" aria-label="Close-up of a yellow notepad with handwritten resolutions and a pen"></div>
  <svg class="post__curve" viewBox="0 0 271 271" aria-hidden="true">
    <path class="band" d="M0 271 L0 233 C60 228 150 216 195 192 C230 174 255 156 271 140 L271 271 Z"/>
    <path class="sliver" d="M0 233 C60 228 140 218 172 218 C120 238 50 256 0 271 Z"/>
  </svg>
  <div class="brand">Brightmoor Academy</div>
  <h2 class="headline">Goede<br>Voornemens<br>die je volhoudt<br>3 tips</h2>
  <div class="format">
    <span class="format__label">blog</span>
    <svg class="format__icon" viewBox="0 0 28 28" aria-hidden="true">
      <path d="M6 3 H17 L22 8 V25 H6 Z"/>
      <path d="M10 12 H18"/>
      <path d="M10 16 H18"/>
      <path d="M10 20 H15"/>
    </svg>
  </div>
</article>

<article class="post post--facts">
  <div class="post__photo" role="img" aria-label="Woman reading, seen from the side, in green tones"></div>
  <svg class="post__curve" viewBox="0 0 271 271" aria-hidden="true">
    <path class="band" d="M0 271 L0 233 C60 228 150 216 195 192 C230 174 255 156 271 140 L271 271 Z"/>
    <path class="sliver" d="M0 233 C60 228 140 218 172 218 C120 238 50 256 0 271 Z"/>
  </svg>
  <div class="brand">Brightmoor Academy</div>
  <h2 class="headline">Gemiddeld<br>haalt slechts<br>20% zijn/haar<br>goede voornemens</h2>
  <div class="format">
    <span class="format__label">facts</span>
    <svg class="format__icon" viewBox="0 0 28 28" aria-hidden="true">
      <circle cx="14" cy="14" r="11"/>
      <circle class="solid" cx="14" cy="8.5" r="1.6"/>
      <path d="M14 13 V20"/>
    </svg>
  </div>
</article>

<article class="post post--podcast">
  <div class="post__photo" role="img" aria-label="Portrait of the podcast guest in blue duotone"></div>
  <svg class="post__curve" viewBox="0 0 271 271" aria-hidden="true">
    <path class="band" d="M0 271 L0 233 C60 228 150 216 195 192 C230 174 255 156 271 140 L271 271 Z"/>
    <path class="sliver" d="M0 233 C60 228 140 218 172 218 C120 238 50 256 0 271 Z"/>
  </svg>
  <div class="brand">Brightmoor Academy</div>
  <p class="subline">Wissel je<br>blik met</p>
  <h2 class="headline">Jorrit<br>Velmaat</h2>
  <div class="format">
    <span class="format__label">podcast</span>
    <svg class="format__icon" viewBox="0 0 28 28" aria-hidden="true">
      <rect x="10" y="3" width="8" height="13" rx="4"/>
      <path d="M6 13 A8 8 0 0 0 22 13"/>
      <path d="M14 21 V25"/>
      <path d="M10 25 H18"/>
    </svg>
  </div>
</article>

</body>
</html>
```